Corvane Voyage Group, Inc
Stationary set
Project: Corvane Voyage Group, Inc
Corvane Voyage Group, Inc - Travel
Creative Brief
Corporate
Peter Talmuddy
President
382 Gorsefield Parkway Suite 519
info@corvanevoyage.com
www.corvanevoyage.com

```html
<!DOCTYPE html>
<html lang="en">
<head>
<meta charset="utf-8">
<title>Corvane Voyage Group, Inc — Stationery Set</title>
<link rel="stylesheet" href="https://fonts.googleapis.com/css2?family=Cinzel:wght@600&family=Arimo:wght@400;700&display=swap">
<style>
  :root {
    --brown: #5b2a18;
    --green: #1f4a36;
    --red: #8a3a1e;
    --ink: #333333;
    --paper: #ffffff;
    --backdrop: #e9e6e1;
    --flap: #111111;
    --rule-green: #2c6a48;
  }
  * { box-sizing: border-box; margin: 0; padding: 0; }
  html, body { width: 1200px; height: 540px; overflow: hidden; }
  body {
    background: var(--backdrop);
    position: relative;
    font-family: "Arimo", Arial, sans-serif;
    color: var(--ink);
  }
  .sheet {
    position: absolute;
    background: var(--paper);
    box-shadow: 0 2px 6px rgba(0,0,0,.18);
    overflow: hidden;
  }
  .brand {
    display: flex;
    flex-direction: column;
    align-items: center;
    gap: 3px;
  }
  .brand-dot {
    border-radius: 50%;
    background: var(--brown);
  }
  .brand-name {
    font-family: "Cinzel", Georgia, serif;
    font-weight: 600;
    color: var(--red);
    white-space: nowrap;
    letter-spacing: .02em;
  }
  .brand-tag {
    font-size: 5px;
    color: var(--red);
    text-transform: uppercase;
    letter-spacing: .08em;
  }

  /* Business cards */
  .card-front { left: 116px; top: 34px; width: 150px; height: 98px; }
  .card-details { position: absolute; left: 48px; top: 10px; font-size: 5.5px; line-height: 1.45; white-space: nowrap; }
  .card-details .person { font-weight: 700; font-size: 6.5px; }
  .card-details .role { margin-bottom: 5px; }
  .card-front .stripe-green { position: absolute; left: 0; right: 0; bottom: 8px; height: 2px; background: var(--green); }
  .card-front .stripe-brown { position: absolute; left: 0; right: 0; bottom: 4px; height: 2px; background: var(--brown); }

  .card-back { width: 156px; height: 91px; top: 137px; display: flex; align-items: center; justify-content: center; }
  .card-back.brown { left: 12px; background: var(--brown); }
  .card-back.green { left: 175px; background: var(--green); }
  .card-back .brand-dot { width: 24px; height: 24px; background: var(--paper); }
  .card-back .brand-name { font-size: 6.5px; color: var(--paper); }

  .card-plain { left: 108px; top: 233px; width: 156px; height: 84px; display: flex; align-items: center; justify-content: center; }
  .card-plain .brand-dot { width: 24px; height: 24px; }
  .card-plain .brand-name { font-size: 6.5px; }

  /* Envelope */
  .envelope { left: 353px; top: 24px; width: 410px; height: 199px; }
  .envelope-flap { position: absolute; left: 0; top: 0; }
  .envelope-mark { position: absolute; left: 50%; top: 8px; width: 30px; height: 30px; margin-left: -15px; border-radius: 50%; background: var(--paper); }
  .envelope-url { position: absolute; left: 116px; top: 134px; font-size: 11px; }

  /* Compliment slip */
  .slip { left: 353px; top: 233px; width: 410px; height: 175px; }
  .slip .brand { position: absolute; left: 18px; top: 18px; }
  .slip .brand-dot { width: 22px; height: 22px; }
  .slip .brand-name { font-size: 6.5px; }
  .slip-address { position: absolute; left: 18px; top: 70px; font-size: 7px; line-height: 1.5; }
  .slip .rule-green { position: absolute; left: 0; right: 0; bottom: 28px; height: 2px; background: var(--rule-green); }
  .slip .rule-brown { position: absolute; left: 0; right: 0; bottom: 24px; height: 2px; background: var(--brown); }

  /* Letterhead */
  .letterhead { left: 785px; top: 19px; width: 408px; height: 504px; }
  .letterhead .brand { position: absolute; left: 0; right: 0; top: 18px; }
  .letterhead .brand-dot { width: 40px; height: 40px; }
  .letterhead .brand-name { font-size: 12px; }
  .letterhead-address { position: absolute; left: 14px; top: 372px; font-size: 9px; line-height: 1.4; }
  .letterhead-address .email { color: var(--red); }
  .letterhead .rule-green { position: absolute; left: 0; right: 0; top: 442px; height: 3px; background: var(--rule-green); }
  .letterhead .rule-brown { position: absolute; left: 0; right: 0; top: 447px; height: 3px; background: var(--brown); }
  .letterhead-url { position: absolute; right: 16px; top: 464px; font-size: 9px; }
  .letterhead-band { position: absolute; left: 0; right: 0; bottom: 0; height: 20px; background: var(--brown); }
</style>
</head>
<body>

  <section class="sheet card-front" aria-label="Business card front">
    <div class="card-details">
      <div class="person">Peter Talmuddy</div>
      <div class="role">President</div>
      <div>382 Gorsefield Parkway</div>
      <div>Suite 519</div>
      <div>Tel: 555-843-0152</div>
      <div>Fax: 555-901-0482</div>
      <div>info@corvanevoyage.com</div>
    </div>
    <span class="stripe-green"></span>
    <span class="stripe-brown"></span>
  </section>

  <section class="sheet card-back brown" aria-label="Business card back, brown">
    <div class="brand"><span class="brand-dot"></span><span class="brand-name">Corvane Voyage Group</span></div>
  </section>

  <section class="sheet card-back green" aria-label="Business card back, green">
    <div class="brand"><span class="brand-dot"></span><span class="brand-name">Corvane Voyage Group</span></div>
  </section>

  <section class="sheet card-plain" aria-label="Business card back, white">
    <div class="brand"><span class="brand-dot"></span><span class="brand-name">Corvane Voyage Group</span></div>
  </section>

  <section class="sheet envelope" aria-label="Envelope">
    <svg class="envelope-flap" width="410" height="46" viewBox="0 0 410 46" aria-hidden="true">
      <polygon points="0,0 410,0 380,46 30,46" fill="var(--flap)"/>
    </svg>
    <span class="envelope-mark"></span>
    <div class="envelope-url">www.corvanevoyage.com</div>
  </section>

  <section class="sheet slip" aria-label="Compliment slip">
    <div class="brand">
      <span class="brand-dot"></span>
      <span class="brand-name">Corvane Voyage Group</span>
      <span class="brand-tag">Travel planned with care</span>
    </div>
    <div class="slip-address">
      <div>382 Gorsefield Parkway</div>
      <div>Suite 519</div>
    </div>
    <span class="rule-green"></span>
    <span class="rule-brown"></span>
  </section>

  <section class="sheet letterhead" aria-label="Letterhead">
    <div class="brand">
      <span class="brand-dot"></span>
      <span class="brand-name">Corvane Voyage Group</span>
      <span class="brand-tag">Travel planned with care</span>
    </div>
    <div class="letterhead-address">
      <div>382 Gorsefield Parkway</div>
      <div>Suite 519</div>
      <div>Cell : 555-843-0152</div>
      <div>Fax : 555-901-0482</div>
      <div class="email">Email : info@corvanevoyage.com</div>
    </div>
    <span class="rule-green"></span>
    <span class="rule-brown"></span>
    <div class="letterhead-url">www.corvanevoyage.com</div>
    <span class="letterhead-band"></span>
  </section>

</body>
</html>
```